Cedar Brook Stables, LLC

Equestrian business card to promote equine retirement, farm sitting, short term board. Located in Aiken, SC.
Updated color schemes.
Contact Information for Business Card
Contact info, description of work.
Colors
0094D4
00A9DD
6FCCEA
C7EBF8
E9F6FB
59FF00
82FF00
B8FF75
E3FFCB
F4FFEA
F0912C
F2A743
F7CA91
FBE8D2
FDF5EE

```html
<!DOCTYPE html>
<html lang="en">
<head>
<meta charset="utf-8">
<title>Cedar Brook Stables — Business Card</title>
<link rel="stylesheet" href="https://fonts.googleapis.com/css2?family=Montserrat:wght@500;700;800&family=Arimo:wght@400;700&display=swap">
<style>
  :root {
    --stage: #2e2e2e;
    --card: #000000;
    --green: #1f8a14;
    --sun: #ffd02e;
    --white: #ffffff;
  }
  * { box-sizing: border-box; margin: 0; padding: 0; }
  html, body { width: 1200px; height: 1015px; overflow: hidden; background: var(--stage); }
  .stage {
    width: 1200px; height: 1015px;
    display: flex; flex-direction: column; align-items: center; justify-content: center; gap: 44px;
  }
  .card {
    width: 780px; height: 445px; background: var(--card);
    box-shadow: 0 14px 30px rgba(0,0,0,.45);
    position: relative; overflow: hidden;
  }
  /* Brand lockup */
  .brand { display: flex; align-items: center; gap: 22px; }
  .brand-dot { border-radius: 50%; background: var(--sun); flex: none; }
  .brand-name {
    font-family: "Montserrat", sans-serif; font-weight: 800; color: var(--white);
    text-transform: uppercase; line-height: 1.08; letter-spacing: .04em;
  }
  /* Front */
  .card-front { display: flex; flex-direction: column; align-items: center; justify-content: center; gap: 62px; }
  .card-front .brand-dot { width: 120px; height: 120px; }
  .card-front .brand-name { font-size: 40px; }
  .services {
    font-family: "Montserrat", sans-serif; font-weight: 700; font-size: 20px; color: var(--white);
    letter-spacing: .04em; text-transform: uppercase; display: flex; align-items: center; gap: 14px;
  }
  .services .sep { width: 9px; height: 9px; border-radius: 50%; background: var(--sun); }
  /* Back */
  .card-back { display: flex; align-items: center; justify-content: space-between; padding: 0 56px 0 70px; }
  .contact { font-family: "Arimo", sans-serif; color: var(--white); }
  .person-name { font-weight: 700; font-size: 30px; color: var(--green); text-transform: uppercase; letter-spacing: .01em; }
  .person-role { font-size: 19px; text-transform: uppercase; margin-top: 2px; }
  .rule { width: 150px; height: 1px; background: var(--green); margin: 22px 0 20px; }
  .contact-list { list-style: none; display: flex; flex-direction: column; gap: 6px; font-size: 21px; }
  .contact-list li { display: flex; align-items: center; gap: 12px; }
  .contact-list svg { width: 20px; height: 20px; flex: none; }
  .address { font-size: 21px; line-height: 1.25; }
  .card-back .brand { flex-direction: column; gap: 18px; text-align: center; }
  .card-back .brand-dot { width: 110px; height: 110px; }
  .card-back .brand-name { font-size: 32px; }
</style>
</head>
<body>
<main class="stage">
  <section class="card card-front" aria-label="Business card front">
    <div class="brand">
      <span class="brand-dot"></span>
      <span class="brand-name">Cedar Brook Stables<br>LLC</span>
    </div>
    <p class="services">
      <span>Short Term Board</span><span class="sep"></span>
      <span>Farm Sitting</span><span class="sep"></span>
      <span>Equine Retirement</span>
    </p>
  </section>

  <section class="card card-back" aria-label="Business card back">
    <div class="contact">
      <h1 class="person-name">Daniel Hayes</h1>
      <p class="person-role">Managing Director</p>
      <div class="rule"></div>
      <ul class="contact-list">
        <li>
          <svg viewBox="0 0 24 24" fill="none" stroke="#1f8a14" stroke-width="2.2"><path d="M5 3h4l2 5-2.5 1.5a11 11 0 0 0 6 6L16 13l5 2v4a2 2 0 0 1-2 2A16 16 0 0 1 3 5a2 2 0 0 1 2-2z"/></svg>
          <span>000-555 014 227</span>
        </li>
        <li>
          <svg viewBox="0 0 24 24" fill="none" stroke="#1f8a14" stroke-width="2.2"><rect x="2" y="5" width="20" height="14"/><path d="M2 6l10 7 10-7"/></svg>
          <span>hello@cedarbrook.example</span>
        </li>
        <li>
          <svg viewBox="0 0 24 24" fill="none" stroke="#1f8a14" stroke-width="2"><circle cx="12" cy="12" r="10"/><path d="M2 12h20M12 2c3 3 3 17 0 20M12 2c-3 3-3 17 0 20"/></svg>
          <span>www.cedarbrook.example</span>
        </li>
      </ul>
      <div class="rule"></div>
      <p class="address">00 Sample Meadow Lane<br>Sampletown, SC 00000</p>
    </div>
    <div class="brand">
      <span class="brand-dot"></span>
      <span class="brand-name">Cedar Brook<br>Stables<br>LLC</span>
    </div>
  </section>
</main>
</body>
</html>
```